Geschäftspapier PLV
Zielgruppe
In den letzten Jahren konnten wir uns durch viel Engagement und Ehrgeiz zum Marktführer im Bereich Kaschierungen und Beschichtungen für den Automobilinnenraum in Europa entwickeln. Angeboten werden Rollenware sowie der Zuschnitt und die Weiterverarbeitung von kaschierten Verbundmaterialien und deren Entwicklung für den jeweiligen Einsatzzweck.
Die vielseitig hergestellten Verbundmaterialien aus Textil bis hin zu Kunst- und Echtledern findet man heute in vielen Bauteilen namhafter Automarken, der Flugzeug- und Schienenfahrzeugindustrie sowie in weiteren industriellen, technischen Anwendungen.
Beispiele dafür sind Innenverkleidungen und Sitze im Fahrzeug, Sonnenschutzkomponenten für den privaten und industriellen Bedarf, wie auch Bezüge von Kindersitzen oder medizinische Hygieneprodukte.
Aufgabenstellung
Zur Darstellung des Unternehmens wird ein neues Geschäftspapier gesucht. Dies sollte die folgenden Informationen zum Unternehmen, sowie die Bankkontakte enthalten. Ebenso sollte das vorhandene Firmenlogo integriert werden.
Das Unternehmen produziert hochwertige Textil-Produkte aus den Bereichen Automarken, der Flugzeug- und Schienenfahrzeugindustrie sowie in weiteren industriellen, technischen Anwendungen.
Das Geschäftspapier sollte diese Eigenschaft widerspiegeln und luxuriös, sowie modern erscheinen.
[Optional]
145 Jahre Erfahrung in der Textilveredlung - Führende Kaschier- und Beschichtungstechnologie
145 years of experience in textile processing - Leading technology in lamination and coating
Unternehmensfarbe Grün:
HKS 61 K
70% Cyan
0% Magenta
100% Gelb
75 % Schwarz
optionale Werbefarbe Anthrazit:
77% Cyan
72% Magenta
67% Gelb
84% Schwarz
Schriftart:
Arial

```html
<!DOCTYPE html>
<html lang="de">
<head>
<meta charset="utf-8">
<title>Geschäftspapier P. L. Vogt GmbH</title>
<link rel="stylesheet" href="https://fonts.googleapis.com/css2?family=Arimo:wght@400;700&display=swap">
<style>
  :root {
    --brand-green: #2f5a1c;
    --anthracite: #1e1e1e;
    --text: #2a2a2a;
    --paper: #ffffff;
  }
  * { margin: 0; padding: 0; box-sizing: border-box; }
  html, body { width: 956px; height: 1200px; overflow: hidden; background: var(--paper); }
  body { font-family: "Arimo", Arial, sans-serif; color: var(--text); }
  .letter { position: relative; width: 956px; height: 1200px; background: var(--paper); }

  .brand-name {
    position: absolute; left: 200px; top: 58px;
    font-size: 60px; font-weight: 700; color: var(--brand-green);
    line-height: 1;
  }

  .sender-line {
    position: absolute; left: 102px; top: 200px;
    font-size: 9.5px; font-weight: 700; color: var(--anthracite);
  }

  .recipient {
    position: absolute; left: 102px; top: 228px;
    font-size: 13px; line-height: 17px; font-style: normal;
  }
  .recipient .city { margin-top: 17px; }

  .sidebar {
    position: absolute; left: 700px; top: 198px; width: 182px;
    text-align: right; font-size: 10.5px; line-height: 13.5px; color: var(--anthracite);
  }
  .sidebar .block { margin-bottom: 15px; }
  .sidebar .label { color: var(--brand-green); font-weight: 700; font-size: 9.5px; }
  .sidebar .strong { font-weight: 700; }
  .contacts { width: 125px; margin-left: auto; }
  .contact-row { display: flex; justify-content: space-between; align-items: center; }
  .contact-row svg { width: 9px; height: 9px; fill: var(--anthracite); }

  .salutation { position: absolute; left: 102px; top: 364px; font-size: 13.5px; }
  .body-copy {
    position: absolute; left: 102px; top: 452px; width: 520px;
    font-size: 13.5px; line-height: 21.4px; text-align: left;
  }
  .closing { position: absolute; left: 102px; top: 862px; font-size: 13.5px; }

  .bank-table {
    position: absolute; left: 102px; top: 1074px;
    border-collapse: collapse; font-size: 9.5px; font-weight: 700; line-height: 13px;
    color: var(--anthracite);
  }
  .bank-table td { padding: 0 12px 0 0; white-space: nowrap; }
  .bank-table .bank { color: var(--brand-green); width: 160px; }
  .bank-table .key { padding-right: 6px; }

  .dot-field {
    position: absolute; right: 0; bottom: 0; width: 290px; height: 300px;
    background: radial-gradient(circle at 100% 100%, rgba(150,150,150,0.45) 0%, rgba(170,170,170,0.2) 50%, rgba(255,255,255,0) 78%);
  }
</style>
</head>
<body>
<main class="letter">
  <div class="brand-name">P. L. Vogt</div>

  <p class="sender-line">P. L. Vogt GmbH · Werkstraße 4 · D-09123 Lindenau</p>

  <address class="recipient">
    Frau<br>Bettina Mustermann<br>Musterstrasse 1
    <div class="city">12345 Musterstadt</div>
  </address>

  <aside class="sidebar">
    <div class="block"><span class="strong">P. L. Vogt GmbH</span><br>Werkstraße 4<br>D-09123 Lindenau</div>
    <div class="block"><span class="label">Postanschrift</span><br>Postfach 2210<br>D-08100 Birkenfeld</div>
    <div class="block contacts">
      <div class="contact-row"><svg viewBox="0 0 10 10"><path d="M2 0h2l1 3-1.5 1a6 6 0 0 0 2.5 2.5L7 5l3 1v2a2 2 0 0 1-2 2A8 8 0 0 1 0 2a2 2 0 0 1 2-2z"/></svg><span>+49 3700 4512 0</span></div>
      <div class="contact-row"><svg viewBox="0 0 10 10"><path d="M1 3h8v6H1zM3 0h4v3H3z"/></svg><span>+49 3700 4512 199</span></div>
      <div class="contact-row"><svg viewBox="0 0 10 10"><circle cx="5" cy="5" r="5"/></svg><span>www.plvogt-textil.de</span></div>
      <div class="contact-row"><svg viewBox="0 0 10 10"><circle cx="5" cy="5" r="5"/></svg><span>post@plvogt-textil.de</span></div>
    </div>
    <div class="block"><span class="label">Handelsregister</span><br>HRB 5190 AG Talberg<br>USt-IdNr.: DE 208764531</div>
    <div class="block"><span class="label">Geschäftsführer</span><br>Jonas Keller</div>
    <div class="block"><span class="label">Prokura</span><br>Lena Hofmann, Max Seidel</div>
  </aside>

  <p class="salutation">Sehr geehrte Frau Mustermann,</p>

  <p class="body-copy">Lorem ipsum dolor sit amet, consetetur sadipscing elitr, sed diam nonumy eirmod tempor invidunt ut labore et dolore magna aliquyam erat, sed diam voluptua. At vero eos et accusam et justo duo dolores et ea rebum. Stet clita kasd gubergren, no sea takimata sanctus est Lorem ipsum dolor sit amet. Lorem ipsum dolor sit amet, consetetur sadipscing elitr, sed diam nonumy eirmod tempor invidunt ut labore et dolore magna aliquyam erat, sed diam voluptua. At vero eos et accusam et justo duo dolores et ea rebum. Stet clita kasd gubergren, no sea takimata sanctus est Lorem ipsum dolor sit amet. Lorem ipsum dolor sit amet, consetetur sadipscing elitr, sed diam nonumy eirmod tempor invidunt ut labore et dolore magna aliquyam erat, sed diam voluptua. At vero eos et accusam et justo duo dolores et ea rebum. Stet clita kasd gubergren, no sea takimata sanctus est Lorem ipsum dolor sit amet. Lorem ipsum dolor sit amet, consetetur sadipscing elitr, sed diam nonumy eirmod tempor invidunt ut labore et dolore magna aliquyam erat, sed diam voluptua. At vero eos et accusam et justo duo dolores et ea rebum. Stet clita kasd gubergren, no sea takimata sanctus est Lorem ipsum dolor sit amet.</p>

  <p class="closing">Mit freundlichen Grüßen</p>

  <table class="bank-table">
    <tr><td class="bank">Sparkasse Talland</td><td class="key">IBAN:</td><td>DE12 3456 7000 0012 3456 78</td><td class="key">BIC:</td><td>TALLDE81XXX</td></tr>
    <tr><td class="bank">Handelsbank Auenburg</td><td class="key">IBAN:</td><td>DE45 6780 1000 0234 5678 90</td><td class="key">BIC:</td><td>HABADEFFXXX</td></tr>
    <tr><td class="bank">Stadtbank Lindenau</td><td class="key">IBAN:</td><td>DE78 9012 3000 0345 6789 01</td><td class="key">BIC:</td><td>STLIDEMMXXX</td></tr>
    <tr><td class="bank">Genossenschaftsbank Talberg</td><td class="key">IBAN:</td><td>DE31 2345 6000 0456 7890 12</td><td class="key">BIC:</td><td>GETADEF1XXX</td></tr>
    <tr><td class="bank">Weidenauer Kreditbank</td><td class="key">IBAN:</td><td>DE64 5678 9000 0567 8901 23</td><td class="key">BIC:</td><td>WEKRDECCXXX</td></tr>
  </table>

  <div class="dot-field" role="img" aria-label="Dekoratives graues Punktraster, das sich von der unteren rechten Ecke fächerförmig ausbreitet"></div>
</main>
</body>
</html>
```